Website Revamp: Favorzo.com

Just got a new logo looking for a web design to go with the business. I need the photoshop files and stock photos. No Word Press Please.

```html
<!DOCTYPE html>
<html lang="en">
<head>
<meta charset="utf-8">
<title>Favorzo Auto Recycling</title>
<link href="https://fonts.googleapis.com/css2?family=Nunito:ital,wght@0,300;0,400;0,600;0,700;0,800;1,400&family=Open+Sans:ital,wght@1,400&display=swap" rel="stylesheet">
<style>
:root{
  --green:#8dc63f;
  --navy:#2c3040;
  --blue:#3b3f8e;
  --link:#2b4c9a;
  --ink:#222;
  --muted:#8a8a8a;
  --line:#e6e6e6;
  --soft:#f4f4f4;
  --white:#fff;
}
*{box-sizing:border-box;margin:0;padding:0}
html,body{width:1200px;height:4847px;overflow:hidden}
body{position:relative;font-family:'Nunito',sans-serif;color:var(--ink);background:var(--white)}
.abs{position:absolute}
section,header,footer,nav{position:absolute;left:0;width:1200px}

.topbar{top:0;height:49px;background:var(--navy);color:#cfd2dc;font-size:14px}
.topbar .hours{left:68px;top:15px}
.social{display:flex;gap:14px}
.social span{width:11px;height:11px;border-radius:50%;background:currentColor;display:block}
.topbar .social{right:58px;top:19px;color:#cfd2dc}

.site-header{top:49px;height:139px}
.brand{left:56px;top:26px;display:flex;align-items:center;gap:10px}
.brand .mark{width:74px;height:74px;border-radius:50%;background:var(--green)}
.brand .name{font-size:38px;font-weight:800;color:var(--green);line-height:1}
.brand .tag{font-size:12px;letter-spacing:4px;color:var(--green);font-weight:800}
.info{display:flex;gap:22px;align-items:flex-start}
.info h4{font-size:18px;font-weight:700;color:var(--ink)}
.info p{font-size:14px;color:var(--muted);margin-top:4px}
.hexicon{width:48px;height:52px;flex:none}
.info.addr{left:357px;top:42px}
.info.mail{left:613px;top:42px}
.divider-v{left:582px;top:40px;width:1px;height:60px;background:var(--line)}
.btn-appoint{left:899px;top:49px;width:218px;height:41px;border:1px solid var(--line);border-radius:3px;font-size:14px;font-weight:800;color:var(--link);display:flex;align-items:center;justify-content:center}

.main-nav{top:188px;height:79px;background:var(--green)}
.main-nav ul{list-style:none;display:flex;position:absolute;left:56px;top:0;height:79px}
.main-nav li{color:#fff;font-size:14px;font-weight:600;padding:0 17px;display:flex;align-items:center;border-right:2px solid rgba(255,255,255,.55)}
.main-nav li:first-child{padding-left:14px;opacity:.7}
.main-nav .caret{font-size:9px;margin-left:5px}
.call{right:96px;top:23px;font-size:24px;font-weight:800;color:#fff;display:flex;align-items:center;gap:10px}
.call .lbl{color:#c9e59c}

.hero{top:267px;height:549px}
.hero .photo{position:absolute;inset:0;background:radial-gradient(ellipse at 72% 55%,#8c9196 0%,#6f767d 45%,#5f666d 100%)}
.hero h1{left:56px;top:95px;font-size:36px;font-weight:300;color:#fff;line-height:42px}
.hero .sub{left:56px;top:194px;font-size:10px;color:#e6e8eb}
.btn-read{left:56px;top:245px;width:100px;height:26px;border-radius:13px;background:var(--blue);color:#fff;font-size:8px;font-weight:700;display:flex;align-items:center;justify-content:center}

.title-c{width:100%;text-align:center;font-size:34px;font-weight:600}
.rule{height:3px;width:62px;background:var(--blue)}
.rule::after{content:"";display:block;height:2px;width:100%;margin-top:5px;background:var(--blue);opacity:.6}
.title-l{font-size:32px;font-weight:700}

.welcome{top:816px;height:698px}
.welcome .title-c{top:70px}
.welcome .rule{left:569px;top:124px}
.welcome .lead{top:168px;width:100%;text-align:center;font-size:16px;color:var(--muted);line-height:30px}
.feature{top:290px;width:335px;height:295px;border:1px solid var(--line);text-align:center}
.feature .hexicon{width:94px;height:100px;margin:46px auto 0;display:block}
.feature h3{font-size:18px;font-weight:700;margin-top:26px}
.feature p{font-size:14px;color:var(--muted);line-height:25px;margin-top:10px;padding:0 34px}

.quote-band{top:1514px;height:107px;background:var(--soft)}
.quote-band p{left:68px;top:38px;font-family:'Open Sans',sans-serif;font-style:italic;font-size:22px;color:var(--ink)}
.btn-outline{border:2px solid #e1e1e1;border-radius:22px;background:#fff;color:var(--link);font-size:13px;font-weight:800;display:flex;align-items:center;justify-content:center}
.quote-band .btn-outline{left:890px;top:32px;width:218px;height:45px}

.arrows{width:114px;height:44px;background:var(--green);display:flex;color:#fff;font-size:14px}
.arrows span{flex:1;display:flex;align-items:center;justify-content:center}

.services{top:1621px;height:599px}
.services .title-l{left:68px;top:70px}
.services .rule{left:68px;top:120px}
.services .arrows{left:1018px;top:126px}
.svc{top:168px;width:243px;height:355px;border:1px solid var(--line);background:#fff}
.svc .ph{height:160px}
.svc .head{display:flex;justify-content:space-between;align-items:center;padding:14px 22px 12px;border-bottom:1px solid var(--line)}
.svc h3{font-size:18px;font-weight:700}
.svc .ico{width:24px;height:22px;background:var(--navy);border-radius:4px}
.svc p{font-size:14px;color:var(--muted);line-height:25px;padding:18px 22px 0}

.appoint{top:2220px;height:633px;background:var(--green)}
.appoint .title-l{left:68px;top:74px;color:var(--navy)}
.appoint .rule{left:68px;top:122px}
.form-box{left:68px;top:167px;width:700px;height:369px;border:2px solid rgba(255,255,255,.75)}
.field{border:1px solid rgba(255,255,255,.75);height:43px;color:rgba(255,255,255,.6);font-size:13px;padding:9px 14px}
.btn-submit{left:30px;top:292px;width:145px;height:41px;border-radius:21px;background:#fff;color:var(--navy);font-size:13px;font-weight:800;display:flex;align-items:center;justify-content:center}
.perk{left:801px;display:flex;gap:22px}
.perk svg{width:36px;height:44px;flex:none}
.perk h4{font-size:17px;font-weight:700;color:var(--navy)}
.perk .s{font-size:15px;color:var(--link);margin-top:4px}
.perk .d{font-size:14px;color:rgba(255,255,255,.55);line-height:25px;margin-top:8px;width:275px}

.feedback{top:2853px;height:600px}
.feedback .title-l{left:68px;top:70px}
.feedback .rule{left:68px;top:122px}
.feedback .arrows{left:1018px;top:112px}
.review{top:170px;width:502px;height:282px;background:#fff;box-shadow:0 2px 10px rgba(0,0,0,.08)}
.review .avatar{left:19px;top:13px;width:77px;height:71px;background:linear-gradient(#d8dbe0,#9aa2ad)}
.review .who{left:124px;top:37px;font-size:18px;font-weight:700}
.review .who em{font-weight:400;color:var(--muted)}
.review .stars{left:387px;top:37px;color:#f5b400;font-size:14px;letter-spacing:2px}
.review .txt{left:19px;top:124px;width:470px;font-style:italic;font-size:15px;color:var(--muted);line-height:29px}
.review .tag{left:19px;top:246px;font-size:16px;font-weight:700;color:var(--link)}
.review .badge{left:415px;top:245px;width:66px;height:22px;border-radius:11px;background:var(--navy)}
.car-strip{left:18px;top:452px;width:1164px;height:147px;background:linear-gradient(180deg,#d4d7db 0%,#a9aeb4 100%)}

.news{top:3453px;height:667px}
.news .title-c{top:30px}
.news .rule{left:569px;top:86px}
.post{top:127px;width:335px;border:1px solid var(--line);background:#fff;padding:22px 22px 30px}
.post .ph{height:160px}
.post h3{font-size:18px;font-weight:700;line-height:26px;margin-top:20px}
.post p{font-size:14px;color:var(--muted);line-height:25px;margin-top:12px}
.post .meta{font-size:14px;color:var(--muted);font-style:italic;margin-top:26px;padding-left:22px}

.partners{top:4120px;height:169px;background:#fbfbfb}
.partner{top:43px;width:117px;height:83px;border:1px solid #ececec;background:#fff;display:flex;align-items:center;justify-content:center}
.partner span{width:70px;height:26px;border-radius:13px;background:#dcdcdc}

.site-footer{top:4319px;height:459px;background:var(--green);color:#fff}
.f-logo{left:94px;top:49px;width:94px;height:94px;border-radius:50%;background:rgba(255,255,255,.35)}
.f-name{left:68px;top:150px;font-size:34px;font-weight:800}
.f-about{left:68px;top:207px;width:250px;font-size:15px;line-height:21px;color:var(--navy)}
.f-btn{left:68px;top:337px;width:220px;height:43px;border:2px solid #fff;border-radius:22px;font-size:13px;font-weight:800;display:flex;align-items:center;justify-content:center}
.f-col h4{font-size:17px;font-weight:700}
.f-blog{left:340px;top:84px;width:245px}
.f-blog .t{font-size:14px;color:rgba(255,255,255,.55);margin-top:40px}
.f-blog .d{font-size:13px;font-style:italic;color:var(--navy);margin-top:14px;padding-bottom:20px;border-bottom:1px solid rgba(255,255,255,.6)}
.f-blog .d.last{border:0}
.f-contact{left:615px;top:84px}
.f-contact ul{list-style:none;margin-top:34px}
.f-contact li{font-size:15px;color:var(--navy);display:flex;gap:14px;align-items:center;height:40px}
.f-contact li i{width:12px;height:12px;background:rgba(255,255,255,.6);border-radius:2px;display:block}
.f-contact .map{font-size:14px;color:var(--navy);text-decoration:underline;margin-top:8px}
.f-hours{left:888px;top:84px;width:245px}
.f-hours ul{list-style:none;margin-top:22px}
.f-hours li{display:flex;justify-content:space-between;font-size:15px;color:var(--navy);height:30.7px;align-items:center}

.bottom{top:4778px;height:69px;background:#fff;font-size:14px;color:var(--muted)}
.bottom p{left:68px;top:25px}
.bottom .social{right:90px;top:30px;color:var(--navy);gap:40px}
</style>
</head>
<body>

<div class="abs topbar" style="left:0;width:1200px">
  <span class="abs hours">◷ &nbsp;We're Open: Monday - Saturday, 9:00 am - 18:00 pm</span>
  <div class="abs social"><span></span><span></span><span></span><span></span><span></span></div>
</div>

<header class="site-header">
  <div class="abs brand">
    <div class="mark"></div>
    <div><div class="name">Favorzo</div><div class="tag">AUTO RECYCLING</div></div>
  </div>
  <div class="abs info addr">
    <svg class="hexicon" viewBox="0 0 48 52"><polygon points="24,2 45,14 45,38 24,50 3,38 3,14" fill="none" stroke="#9a9a9a" stroke-width="2"/><path d="M24 17a7 7 0 0 1 7 7c0 5-7 11-7 11s-7-6-7-11a7 7 0 0 1 7-7z" fill="none" stroke="#777" stroke-width="2"/><circle cx="24" cy="24" r="2.5" fill="#777"/></svg>
    <div><h4>Address:</h4><p>Elm St 24, Rivertown</p></div>
  </div>
  <div class="abs divider-v"></div>
  <div class="abs info mail">
    <svg class="hexicon" viewBox="0 0 48 52"><polygon points="24,2 45,14 45,38 24,50 3,38 3,14" fill="none" stroke="#9a9a9a" stroke-width="2"/><rect x="14" y="19" width="20" height="14" fill="none" stroke="#777" stroke-width="2"/><path d="M14 19l10 8 10-8" fill="none" stroke="#777" stroke-width="2"/></svg>
    <div><h4>Email:</h4><p>hello@gearnest.net</p></div>
  </div>
  <div class="abs btn-appoint">GET FREE APPOINTMENT</div>
</header>

<nav class="main-nav">
  <ul>
    <li>Home<span class="caret">▼</span></li>
    <li>About Us<span class="caret">▼</span></li>
    <li>Services<span class="caret">▼</span></li>
    <li>Blog<span class="caret">▼</span></li>
    <li>Contact Us</li>
  </ul>
  <div class="abs call">
    <svg width="26" height="26" viewBox="0 0 24 24"><path d="M6 3l3 4-2 2c1 3 4 6 7 7l2-2 4 3-2 4C10 20 4 14 3 5z" fill="none" stroke="#c9e59c" stroke-width="1.6"/></svg>
    <span><span class="lbl">Call Us:</span> 1-800-555-0147</span>
  </div>
</nav>

<section class="hero">
  <div class="photo" role="img" aria-label="Green and black flatbed tow truck in front of a grey city skyline"></div>
  <h1 class="abs">Auto Salvage Yard<br>We Recycle, Nearly Everything!</h1>
  <p class="abs sub">At times nearly 90% of a vehicle can be salvaged.</p>
  <div class="abs btn-read">READ MORE</div>
</section>

<section class="welcome">
  <h2 class="abs title-c">Welcome to GearNest</h2>
  <div class="abs rule"></div>
  <p class="abs lead">We started GearNest because we believed that the auto repair industry was broken<br>and we trusted earning your trust.</p>
  <div class="abs feature" style="left:68px">
    <svg class="hexicon" viewBox="0 0 94 100"><polygon points="47,3 90,27 90,73 47,97 4,73 4,27" fill="none" stroke="#3b3f8e" stroke-width="3"/><path d="M35 63l24-24M59 63L35 39M31 35l6 6M63 35l-6 6" stroke="#3b3f8e" stroke-width="3" fill="none"/></svg>
    <h3>Vehicle Inspection</h3>
    <p>Receive a free, fast, fair &amp; transparent price quote.</p>
  </div>
  <div class="abs feature" style="left:433px">
    <svg class="hexicon" viewBox="0 0 94 100"><polygon points="47,3 90,27 90,73 47,97 4,73 4,27" fill="none" stroke="#3b3f8e" stroke-width="3"/><rect x="34" y="34" width="26" height="32" fill="none" stroke="#3b3f8e" stroke-width="2.5"/><path d="M39 43h16M39 50h16M39 57h10" stroke="#3b3f8e" stroke-width="2.5"/></svg>
    <h3>Diagnostic Services</h3>
    <p>Provide your home or office location. Tell us when to meet you there.</p>
  </div>
  <div class="abs feature" style="left:797px">
    <svg class="hexicon" viewBox="0 0 94 100"><polygon points="47,3 90,27 90,73 47,97 4,73 4,27" fill="none" stroke="#3b3f8e" stroke-width="3"/><circle cx="47" cy="50" r="12" fill="none" stroke="#3b3f8e" stroke-width="3" stroke-dasharray="5 3"/><circle cx="47" cy="50" r="5" fill="none" stroke="#3b3f8e" stroke-width="2.5"/></svg>
    <h3>Serrvice Upgrades</h3>
    <p>No more waiting in repair shops, we will reach your destination in one call.</p>
  </div>
</section>

<section class="quote-band">
  <p class="abs">We provide them access to customers, flexibility, and high-quality parts.</p>
  <div class="abs btn-outline">GET A QUOTE</div>
</section>

<section class="services">
  <h2 class="abs title-l">Our Services</h2>
  <div class="abs rule"></div>
  <div class="abs arrows"><span>‹</span><span>›</span></div>
  <div class="abs svc" style="left:79px">
    <div class="ph" role="img" aria-label="Orange flatbed truck carrying a car" style="background:linear-gradient(135deg,#c9cfd6,#e59a2c 55%,#6b7078)"></div>
    <div class="head"><h3>Engine Works</h3><span class="ico"></span></div>
    <p>Engine service is an auto mobile window and talent high quality paint and materials.</p>
  </div>
  <div class="abs svc" style="left:346px">
    <div class="ph" role="img" aria-label="Crushed red car lifted by a crane" style="background:linear-gradient(135deg,#7d94b4,#b62a2a 55%,#3c3f45)"></div>
    <div class="head"><h3>Air Conditioner</h3><span class="ico"></span></div>
    <p>A car cooler is an auto mobile window evaporative cooler and sometimes as a swamp.</p>
  </div>
  <div class="abs svc" style="left:613px">
    <div class="ph" role="img" aria-label="Tow truck towing a car on a road at sunset" style="background:linear-gradient(180deg,#6a8fc4,#f0c069 60%,#8a8278)"></div>
    <div class="head"><h3>Wheel Works</h3><span class="ico" style="border-radius:50%"></span></div>
    <p>We guarantee the best price on all tires and offer free services like tire rotations.</p>
  </div>
  <div class="abs svc" style="left:880px">
    <div class="ph" role="img" aria-label="White car loaded on a tow truck" style="background:linear-gradient(135deg,#b7c6d8,#eef0f2 55%,#7b8087)"></div>
    <div class="head"><h3>Painting Works</h3><span class="ico" style="width:16px"></span></div>
    <p>Auto body painting means you can pursue entry level positions with our employers.</p>
  </div>
</section>

<section class="appoint">
  <h2 class="abs title-l">Get an Appoinment</h2>
  <div class="abs rule"></div>
  <div class="abs form-box">
    <div class="abs field" style="left:30px;top:30px;width:305px">Name</div>
    <div class="abs field" style="left:365px;top:30px;width:305px">Email</div>
    <div class="abs field" style="left:30px;top:96px;width:305px">Phone</div>
    <div class="abs field" style="left:365px;top:96px;width:305px">Subject</div>
    <div class="abs field" style="left:30px;top:162px;width:640px;height:107px">Message</div>
    <div class="abs btn-submit">SUBMIT NOW</div>
  </div>
  <div class="abs perk" style="top:172px">
    <svg viewBox="0 0 36 44"><circle cx="18" cy="9" r="6" fill="none" stroke="#2c3040" stroke-width="2.5"/><path d="M6 42V24l12-6 12 6v18M12 30v12M24 30v12" fill="none" stroke="#2c3040" stroke-width="2.5"/></svg>
    <div><h4>Best Material Used</h4><p class="s">Desires to obtain</p><p class="d">How all this mistakens idea denouncing pleasures and completed account.</p></div>
  </div>
  <div class="abs perk" style="top:311px">
    <svg viewBox="0 0 36 44"><circle cx="18" cy="12" r="8" fill="none" stroke="#2c3040" stroke-width="2.5"/><path d="M4 42c0-10 6-16 14-16s14 6 14 16z" fill="none" stroke="#2c3040" stroke-width="2.5"/></svg>
    <div><h4>Expert Mechanics</h4><p class="s">Resultant pleasure</p><p class="d">There anyone who loves or pursues or desires to obtain pain of itself.</p></div>
  </div>
  <div class="abs perk" style="top:449px">
    <svg viewBox="0 0 36 44"><circle cx="18" cy="14" r="10" fill="none" stroke="#2c3040" stroke-width="2.5"/><path d="M11 22l-6 18 7-3 4 6 2-10M25 22l6 18-7-3-4 6-2-10" fill="none" stroke="#2c3040" stroke-width="2"/></svg>
    <div><h4>Certified Detailers</h4><p class="s">Ever undertakes</p><p class="d">Take a trivial example, which of us ever sets laborious physical exercise.</p></div>
  </div>
</section>

<section class="feedback">
  <h2 class="abs title-l">Customer Feedback</h2>
  <div class="abs rule"></div>
  <div class="abs arrows"><span>‹</span><span>›</span></div>
  <div class="abs review" style="left:83px">
    <div class="abs avatar" role="img" aria-label="Customer portrait"></div>
    <p class="abs who">Dana Reyes - <em>London</em></p>
    <span class="abs stars">★★★★★</span>
    <p class="abs txt">" They did all the repairs and it cost me about 1/3 of the price. I was actually really happy with the work that was done. They were aware of our transported for road.</p>
    <p class="abs tag">Changed Oil and Filter</p>
    <span class="abs badge"></span>
  </div>
  <div class="abs review" style="left:615px">
    <div class="abs avatar" role="img" aria-label="Customer portrait"></div>
    <p class="abs who">Dana Reyes - <em>London</em></p>
    <span class="abs stars">★★★★★</span>
    <p class="abs txt">" They did all the repairs and it cost me about 1/3 of the price. I was actually really happy with the work that was done. They were aware of our transported for road.</p>
    <p class="abs tag">Changed Oil and Filter</p>
    <span class="abs badge"></span>
  </div>
  <div class="abs car-strip" role="img" aria-label="Side view of a silver car with green accents"></div>
</section>

<section class="news">
  <h2 class="abs title-c">Latest News</h2>
  <div class="abs rule"></div>
  <article class="abs post" style="left:68px">
    <div class="ph" role="img" aria-label="Red sports coupe at dusk" style="background:linear-gradient(180deg,#d98a4a,#7a1d22 60%,#2a2a2e)"></div>
    <h3>Simulation of Customers' Booking Behavior...</h3>
    <p>Simulation helps us out when we want to find out more about a crystal ball helpin</p>
    <p class="meta">05 August 2019 &nbsp;&nbsp; Ray Holt</p>
  </article>
  <article class="abs post" style="left:433px">
    <div class="ph" role="img" aria-label="White car with a red roof in a showroom" style="background:linear-gradient(135deg,#3a3d42,#e8e8e8 50%,#c0262b 70%,#2c2f34)"></div>
    <h3>Get Some Usefull Car Maintanance Tips From Our Expets</h3>
    <p>Simulation helps us out when we want to find out more about a crystal ball helpin</p>
    <p class="meta">05 August 2019 &nbsp;&nbsp; Ray Holt</p>
  </article>
  <article class="abs post" style="left:797px">
    <div class="ph" role="img" aria-label="Rows of new cars in a parking lot" style="background:linear-gradient(180deg,#e39b4e,#9fb3c8 50%,#d9dde2)"></div>
    <h3>High Quality Cars Only We Selling to Our Customers</h3>
    <p>Simulation helps us out when we want to find out more about a crystal ball helpin</p>
    <p class="meta">05 August 2019 &nbsp;&nbsp; Ray Holt</p>
  </article>
</section>

<section class="partners">
  <div class="abs partner" style="left:98px"><span></span></div>
  <div class="abs partner" style="left:275px"><span></span></div>
  <div class="abs partner" style="left:451px"><span style="width:40px;height:40px;border-radius:50%"></span></div>
  <div class="abs partner" style="left:628px"><span></span></div>
  <div class="abs partner" style="left:805px"><span></span></div>
  <div class="abs partner" style="left:982px"><span></span></div>
</section>

<footer class="site-footer">
  <div class="abs f-logo"></div>
  <div class="abs f-name">Favorzo</div>
  <p class="abs f-about">Lorem Ipsum is simply dummy text of the printing and typesetting industry. Lorem Ipsum has been the industry's standard dummy text ever since the 1500s.</p>
  <div class="abs f-btn">GET QUOTE NOW</div>
  <div class="abs f-col f-blog">
    <h4>Latest Blog Post</h4>
    <p class="t">Air Filter</p>
    <p class="d">13 August 2019</p>
    <p class="t" style="margin-top:26px">Tool Box</p>
    <p class="d last">13 August 2019</p>
  </div>
  <div class="abs f-col f-contact">
    <h4>Get In Contact</h4>
    <ul>
      <li><i></i>Elm St 24, Rivertown City, USA</li>
      <li><i></i>Phone +44 555 018 274</li>
      <li><i></i>hello@gearnest.net</li>
      <li><i></i>(555) 014-3391</li>
    </ul>
    <p class="map">Find Us On Map</p>
  </div>
  <div class="abs f-col f-hours">
    <h4>Working Hours</h4>
    <ul>
      <li><span>Monday:</span><span>9:30 am - 6.00 pm</span></li>
      <li><span>Tuesday:</span><span>9:30 am - 6.00 pm</span></li>
      <li><span>Wednesday:</span><span>9:30 am - 6.00 pm</span></li>
      <li><span>Thursday:</span><span>9:30 am - 6.00 pm</span></li>
      <li><span>Friday:</span><span>9:30 am - 6.00 pm</span></li>
      <li><span>Saturday:</span><span>9:30 am - 6.00 pm</span></li>
      <li><span>Sunday:</span><span>Closed</span></li>
    </ul>
  </div>
</footer>

<div class="abs bottom" style="left:0;width:1200px">
  <p class="abs">Copyright @ 2020 Favorzo Auto Recycling. All Right Reserved</p>
  <div class="abs social"><span></span><span></span><span></span><span></span></div>
</div>

</body>
</html>
```